AI Layout work for Business Cards, Letterhead and Compliment Slip for Award-winning UK Property Deve

No actual logo or corporate identity design work needed here but some skill required to create layouts for business card, letterhead and compliment slip for this award-winning company.
I can provide AI files featuring the company logo and an initial layout of the business card, (6 versions featuring the same design but for different personnel), along with some initial instructions (with possibly more to follow from the client). The finished layouts for each item need to be print-ready in AI format - 8 in all (6 for each business card plus 1 for letterhead and 1 for compliment slip).
I've given this project a 5-day duration but there may be some flexibility built into that depending on client feedback. Hopefully that won't be a problem.
UPDATE:
The client has been very prescriptive about the layout and design of these. To that end, please find 3 additional pdfs that explain what's required.
1.
All BUSINESS CARDS need to be laid out as per the attached AI file (but see latest pdf to check which layout - there are 2 in the original AI file). Use the details in the RUNE-contact-details.pdf to create 6 individual AI files, one for each card.
2.
Create 2 additional AI files, one each for the LETTERHEAD and the COMPLIMENT SLIP based on the latest mock-up that I've provided (letterhead-layout-final.pdf)
In all, I need EIGHT individual AI files, 6 for each business card, 1 for the letterhead and 1 for the compliment slip. I'd like to get this done as soon as possible now please.
Target Market(s)
Purchasers of upmarket luxury properties - see here: http://www.runeestates.co.uk
Industry/Entity Type
Business
Requirements
Must have
- Layouts need to be cool, understated and uncluttered.
Nice to have
- Please keep it simple! The actual logo background colour is likely to change (awaiting confirmation from client) but accompanying text detail and font (Deja Vu Sans Condensed) can remain as seen in the files below - for the time being at least! That having been said, I'm open to suggestions.
Should not have
- Nothing extreme or ostentatious please.

```html
<!DOCTYPE html>
<html lang="en">
<head>
<meta charset="utf-8">
<title>RUNE Business Card</title>
<link href="https://fonts.googleapis.com/css2?family=PT+Sans:wght@400;700&display=swap" rel="stylesheet">
<style>
  :root {
    --navy: #151f4f;
    --paper: #f7f7f5;
    --ink: #1a1a1a;
    --stage: #dcdcdc;
    --white: #ffffff;
    --rule: #8e95b5;
  }
  * { margin: 0; padding: 0; box-sizing: border-box; }
  html, body { width: 1200px; height: 1200px; overflow: hidden; }
  body {
    background: var(--stage);
    font-family: "PT Sans", "DejaVu Sans Condensed", sans-serif;
    position: relative;
  }
  .card {
    position: absolute;
    left: 260px;
    width: 680px;
    height: 440px;
    overflow: hidden;
  }
  .card--front { top: 150px; background: var(--paper); }
  .card--back  { top: 630px; background: var(--navy); color: var(--white); }

  .name-band {
    position: absolute; left: 0; top: 92px;
    width: 150px; height: 10px; background: var(--navy);
  }
  .role-band {
    position: absolute; left: 265px; top: 108px;
    right: 0; height: 10px; background: var(--navy);
  }
  .person-name {
    position: absolute; left: 150px; top: 60px;
    font-size: 31px; font-weight: 700; color: var(--ink); letter-spacing: 0.5px;
  }
  .person-role {
    position: absolute; left: 150px; top: 98px;
    font-size: 21px; color: var(--ink);
  }
  .contact {
    position: absolute; left: 150px; top: 158px;
    list-style: none; font-size: 18px; line-height: 26px; color: var(--ink);
  }
  .brand-box {
    position: absolute; right: 34px; bottom: 34px;
    width: 190px; height: 120px; background: var(--navy);
    display: flex; align-items: center; justify-content: center;
  }
  .brand-box .brand-name {
    color: var(--white); font-size: 44px; font-weight: 400; letter-spacing: 2px;
  }

  .brand-large {
    position: absolute; left: 60px; top: 150px;
    width: 270px; text-align: center;
    font-size: 86px; font-weight: 400; letter-spacing: 4px; color: var(--white);
  }
  .divider {
    position: absolute; left: 355px; top: 120px;
    width: 1px; height: 200px; background: var(--rule);
  }
  .address {
    position: absolute; left: 385px; top: 152px;
    font-style: normal; font-size: 21px; line-height: 30px; color: var(--white);
  }
</style>
</head>
<body>
  <section class="card card--front" aria-label="Business card front">
    <div class="name-band"></div>
    <div class="role-band"></div>
    <p class="person-name">Daniel Hart</p>
    <p class="person-role">Director</p>
    <ul class="contact">
      <li>+44 (0)1632 960481</li>
      <li>enquiries@runeestates.co.uk</li>
      <li>runeestates.co.uk</li>
    </ul>
    <div class="brand-box"><span class="brand-name">RUNE</span></div>
  </section>

  <section class="card card--back" aria-label="Business card back">
    <p class="brand-large">RUNE</p>
    <div class="divider"></div>
    <address class="address">
      RUNE Exclusive Estates<br>
      Elm Croft House,<br>
      Elm Croft Lane<br>
      Ashbury Green AB1 2CD
    </address>
  </section>
</body>
</html>
```